Lantern

My company name is lantern. The logo is attached. I am the business owner.
Name Gordon Pileck
Phone number- 2018347265
email- Gordon_pileck@mailbrook.net
Website is not live yet but it will be workwithlantern.com
the current beta link is- https://site.qvbtstage.com/lantern-v3/
on the back write “ find creative pros”
Use that beta link as reference for typography and colors on card.

```html
<!DOCTYPE html>
<html lang="en">
<head>
<meta charset="utf-8">
<title>Lantern — Business Card</title>
<link rel="stylesheet" href="https://fonts.googleapis.com/css2?family=Poppins:wght@300;400;700&display=swap">
<style>
  :root {
    --backdrop: #1c1c21;
    --card: #26292c;
    --ink: #e4e4e4;
    --ink-soft: #c9c9c9;
    --accent: #d2572c;
    --rule: #8a8a8a;
    --emboss: #3a3d41;
  }
  * { box-sizing: border-box; margin: 0; padding: 0; }
  html, body { width: 1200px; height: 800px; overflow: hidden; }
  body {
    background: var(--backdrop);
    font-family: "Poppins", sans-serif;
    display: flex;
    align-items: center;
    justify-content: center;
    gap: 40px;
  }
  .card {
    position: relative;
    width: 540px;
    height: 310px;
    background: var(--card);
    border-radius: 22px;
    box-shadow: 0 24px 50px rgba(0,0,0,0.45);
    overflow: hidden;
  }
  .wordmark {
    font-weight: 700;
    text-transform: uppercase;
    color: var(--ink);
    letter-spacing: -1px;
    line-height: 1;
    white-space: nowrap;
  }
  .card--back { display: flex; align-items: center; justify-content: center; }
  .card--back .wordmark { font-size: 74px; color: var(--emboss); }

  .card--front .wordmark {
    position: absolute;
    top: 52px;
    left: 0;
    right: 0;
    text-align: center;
    font-size: 70px;
  }
  .details {
    position: absolute;
    top: 158px;
    left: 30px;
    right: 30px;
    display: flex;
    align-items: center;
    justify-content: center;
  }
  .holder { text-align: right; padding-right: 18px; white-space: nowrap; }
  .holder__name {
    font-weight: 700;
    font-size: 16px;
    color: var(--ink);
    text-transform: uppercase;
    line-height: 1.15;
  }
  .holder__role {
    font-weight: 400;
    font-size: 14px;
    color: var(--accent);
    line-height: 1.3;
  }
  .divider { width: 1px; height: 62px; background: var(--rule); flex: none; }
  .contact { list-style: none; padding-left: 18px; }
  .contact li {
    display: flex;
    align-items: center;
    gap: 9px;
    font-size: 13px;
    font-weight: 400;
    color: var(--ink-soft);
    line-height: 1.7;
    white-space: nowrap;
  }
  .contact svg { width: 12px; height: 12px; fill: var(--accent); flex: none; }
  .tagline {
    position: absolute;
    bottom: 32px;
    left: 0;
    right: 0;
    text-align: center;
    font-size: 13px;
    font-weight: 300;
    letter-spacing: 9px;
    color: var(--ink);
    text-transform: uppercase;
  }
</style>
</head>
<body>
  <section class="card card--back">
    <div class="wordmark">Lantern</div>
  </section>

  <section class="card card--front">
    <div class="wordmark">Lantern</div>
    <div class="details">
      <div class="holder">
        <p class="holder__name">Gordon Pileck</p>
        <p class="holder__role">Business Owner</p>
      </div>
      <div class="divider"></div>
      <ul class="contact">
        <li>
          <svg viewBox="0 0 24 24"><path d="M6.6 10.8a15.1 15.1 0 0 0 6.6 6.6l2.2-2.2a1 1 0 0 1 1-.25 11.4 11.4 0 0 0 3.6.57 1 1 0 0 1 1 1V20a1 1 0 0 1-1 1A17 17 0 0 1 3 4a1 1 0 0 1 1-1h3.5a1 1 0 0 1 1 1c0 1.25.2 2.45.57 3.57a1 1 0 0 1-.25 1z"/></svg>
          2018347265
        </li>
        <li>
          <svg viewBox="0 0 24 24"><path d="M2 5h20v14H2z"/><path d="M2 5l10 8 10-8" fill="none" stroke="#26292c" stroke-width="2"/></svg>
          Gordon_pileck@mailbrook.net
        </li>
        <li>
          <svg viewBox="0 0 24 24"><path d="M12 2a10 10 0 1 0 0 20 10 10 0 0 0 0-20zm6.9 6h-2.9a15.6 15.6 0 0 0-1.4-3.6A8 8 0 0 1 18.9 8zM12 4c.8 1.2 1.5 2.5 1.9 4h-3.8c.4-1.5 1.1-2.8 1.9-4zM4.3 14a8 8 0 0 1 0-4h3.4a16.5 16.5 0 0 0 0 4zm.8 2h2.9c.3 1.3.8 2.5 1.4 3.6A8 8 0 0 1 5.1 16zM8 8H5.1a8 8 0 0 1 4.3-3.6C8.8 5.5 8.3 6.7 8 8zm4 12c-.8-1.2-1.5-2.5-1.9-4h3.8c-.4 1.5-1.1 2.8-1.9 4zm2.3-6H9.7a14.7 14.7 0 0 1 0-4h4.6a14.7 14.7 0 0 1 0 4zm.3 5.6c.6-1.1 1.1-2.3 1.4-3.6h2.9a8 8 0 0 1-4.3 3.6zM16.3 14a16.5 16.5 0 0 0 0-4h3.4a8 8 0 0 1 0 4z"/></svg>
          www.workwithlantern.com
        </li>
      </ul>
    </div>
    <p class="tagline">Find creative pros</p>
  </section>
</body>
</html>
```